Larkfield Circuitry LLC is a Minneapolis / St Paul and surrounding communities computer repair and service company. It serves residential and small businesses. We work primarily with virus removal, data recovery, system baselines, networking, and new system installation. The site should look clean, professional, and easy to navigate.

This wordpress project must be coded and integrated into a wordpress theme for easy upload and maintenance.
Updates

Designers - Please make sure your design is in a wordpress theme so that It can be uploaded.  

Thank you,

Brin 

Target Market(s)

Residential and Small Business

Industry/Entity Type

Residential

Requirements
Must have
• Site Content
1. Main Page should have photos that scroll across, Business Description, Space to run
“Specials” Ads
a. Intuitive Navigation
2. Additional Pages
a. Blog for Computer Repair Articles
b. Testimonials Page
c. Contact Pages
d. Services Page with the ability to put in pricing
3. The site must be clean and professional.
4. Wordpress Theme

```html
<!DOCTYPE html>
<html lang="en">
<head>
<meta charset="utf-8">
<title>Larkfield Circuitry LLC</title>
<link rel="stylesheet" href="https://fonts.googleapis.com/css2?family=Gelasio:wght@400;700&family=Arimo:wght@400;700&display=swap">
<style>
  :root {
    --page-bg: #2c2c2c;
    --panel-bg: #f2f2f2;
    --band-dark: #2d2d2d;
    --box-bg: #e7e7e7;
    --green: #7cb65a;
    --green-dark: #4d7a1f;
    --grey-mid: #777777;
    --grey-light: #b0b0b0;
    --text-dark: #222222;
    --text-body: #3a3a3a;
    --white: #ffffff;
  }
  * { margin: 0; padding: 0; box-sizing: border-box; }
  html, body { width: 866px; height: 1200px; overflow: hidden; }
  body {
    position: relative;
    background: var(--page-bg);
    font-family: "Arimo", Arial, sans-serif;
    color: var(--text-body);
  }
  a { color: inherit; text-decoration: none; }

  /* Header */
  .brand { position: absolute; left: 30px; top: 6px; display: flex; align-items: center; gap: 12px; z-index: 3; }
  .brand-mark { width: 88px; height: 88px; border-radius: 50%; background: var(--green); }
  .brand-name { font-family: "Gelasio", Georgia, serif; font-size: 17px; font-weight: 700; color: var(--grey-light); margin-top: -26px; }

  .main-nav { position: absolute; top: 28px; left: 351px; display: flex; gap: 0; }
  .main-nav a { position: absolute; font-family: "Gelasio", Georgia, serif; font-size: 15px; color: var(--white); white-space: nowrap; top: 0; }
  .main-nav a.is-active { color: #a9a9a9; }
  .nav-pointer { position: absolute; left: 365px; top: 58px; width: 0; height: 0; border-left: 6px solid transparent; border-right: 6px solid transparent; border-bottom: 6px solid var(--panel-bg); z-index: 2; }

  /* Main panel */
  .panel { position: absolute; left: 18px; top: 63px; width: 827px; height: 1059px; background: var(--panel-bg); }

  /* Hero */
  .hero-visual {
    position: absolute; left: 495px; top: 66px; width: 280px; height: 462px;
    background: linear-gradient(160deg, #e2e2e2 0%, #c9c9c9 40%, #efefef 100%);
    border-radius: 4px;
  }
  .hero-lead { position: absolute; font-family: "Arimo", Arial, sans-serif; font-weight: 700; color: var(--grey-light); font-size: 23px; line-height: 24px; text-align: right; left: 150px; top: 157px; width: 168px; }
  .hero-tech { position: absolute; left: 318px; top: 128px; font-family: "Arimo", Arial, sans-serif; font-weight: 700; font-size: 76px; letter-spacing: -3px; color: var(--grey-mid); }
  .hero-title { position: absolute; left: 86px; top: 196px; font-family: "Gelasio", Georgia, serif; font-weight: 700; font-size: 80px; color: var(--green); letter-spacing: -1px; }
  .hero-sub { position: absolute; left: 269px; top: 285px; font-family: "Arimo", Arial, sans-serif; font-weight: 700; font-size: 15.5px; color: var(--grey-light); }
  .hero-copy { position: absolute; left: 94px; top: 319px; width: 372px; font-size: 7px; line-height: 9.5px; color: var(--text-dark); }
  .btn-learn { position: absolute; left: 351px; top: 355px; width: 115px; height: 27px; background: #4a4a4a; color: var(--white); font-weight: 700; font-size: 14.5px; display: flex; align-items: center; padding-left: 7px; gap: 9px; }
  .btn-learn svg { width: 7px; height: 10px; }
  .slider-dots { position: absolute; left: 99px; top: 464px; display: flex; gap: 6px; }
  .slider-dots span { width: 16px; height: 16px; border-radius: 50%; background: #4a4a4a; }
  .slider-dots span.is-current { background: #c4c4c4; }

  /* Service band */
  .service-band { position: absolute; left: 93px; top: 549px; width: 677px; height: 190px; background: var(--box-bg); }
  .service-band-head { height: 52px; background: var(--band-dark); }
  .service-col { position: absolute; top: 0; }
  .service-col h3 { font-family: "Gelasio", Georgia, serif; font-weight: 400; font-size: 15px; line-height: 18px; color: var(--white); margin-top: 9px; height: 43px; }
  .service-col ul { list-style: none; margin-top: 3px; }
  .service-col li { position: absolute; font-size: 13px; color: #444; white-space: nowrap; }
  .service-col li::before { content: ""; position: absolute; left: -13px; top: 3px; border-top: 5px solid transparent; border-bottom: 5px solid transparent; border-left: 6px solid var(--white); }
  .read-more { position: absolute; top: 167px; font-size: 13px; color: var(--green-dark); white-space: nowrap; }

  /* Info boxes */
  .info-box { position: absolute; top: 768px; width: 216px; height: 267px; background: var(--box-bg); }
  .info-box h2 { height: 31px; background: var(--band-dark); color: var(--white); font-family: "Gelasio", Georgia, serif; font-weight: 400; font-size: 15px; line-height: 31px; padding-left: 9px; }
  .info-body { padding: 18px 14px 0 22px; }
  .info-intro { font-size: 10px; line-height: 11.5px; color: #000; margin-bottom: 23px; }
  .info-text { font-size: 7px; line-height: 9.5px; color: var(--text-dark); margin-bottom: 10px; }
  .info-more { font-size: 8px; color: var(--green-dark); display: block; margin-top: 14px; }
  .info-list { list-style: none; margin-top: -6px; }
  .info-list li { position: relative; font-size: 7px; color: var(--text-dark); height: 24.5px; padding-left: 12px; }
  .info-list li::before { content: ""; position: absolute; left: 0; top: 1px; border-top: 3.5px solid transparent; border-bottom: 3.5px solid transparent; border-left: 4px solid #000; }

  /* Footer */
  .site-footer { position: absolute; left: 0; top: 1122px; width: 866px; height: 31px; }
  .copyright { position: absolute; left: 83px; top: 10px; font-family: "Gelasio", Georgia, serif; font-size: 12px; color: #b5b5b5; white-space: nowrap; }
  .footer-nav a { position: absolute; top: 8px; font-family: "Gelasio", Georgia, serif; font-size: 12px; color: #c4c4c4; white-space: nowrap; }
  .footer-strip { position: absolute; left: 18px; top: 1153px; width: 827px; height: 25px; background: var(--panel-bg); }
</style>
</head>
<body>

<header class="site-header">
  <div class="brand">
    <div class="brand-mark"></div>
    <span class="brand-name">Larkfield Circuitry LLC</span>
  </div>
  <nav class="main-nav">
    <a href="#" class="is-active" style="left:0">Home</a>
    <a href="#" style="left:61px">About</a>
    <a href="#" style="left:122px">Services</a>
    <a href="#" style="left:194px">Data Recovery</a>
    <a href="#" style="left:309px">Testimonials</a>
    <a href="#" style="left:414px">Contacts</a>
  </nav>
</header>

<main class="panel"></main>
<div class="nav-pointer"></div>

<section class="hero">
  <div class="hero-visual" role="img" aria-label="Silver all-in-one desktop computer with wireless keyboard and mouse"></div>
  <div class="hero-lead">OFFERING<br>EXCELLENT</div>
  <div class="hero-tech">tech</div>
  <h1 class="hero-title">SUPPORT</h1>
  <div class="hero-sub">AT COMPETITIVE PRICES</div>
  <p class="hero-copy">We repair, clean and set up home and office computers across Minneapolis, St Paul and the surrounding communities. Our technicians remove viruses, recover lost files, build system baselines and install new machines and networks quickly, carefully and at fair prices, so you can get back to work and life without the worry.</p>
  <a href="#" class="btn-learn">Learn More
    <svg viewBox="0 0 7 10"><path d="M0 0 L7 5 L0 10 Z" fill="#ffffff"/></svg>
  </a>
  <div class="slider-dots"><span></span><span></span><span class="is-current"></span><span></span></div>
</section>

<section class="service-band">
  <div class="service-band-head"></div>
  <div class="service-col" style="left:23px">
    <h3>Home Computer<br>Services</h3>
    <ul>
      <li style="left:3px;top:58px">Recovery</li>
      <li style="left:3px;top:82px">Virus Removal</li>
      <li style="left:3px;top:106px">System Installation</li>
      <li style="left:3px;top:131px">Data Recovery</li>
    </ul>
  </div>
  <div class="service-col" style="left:190px">
    <h3>Small Business<br>Computer Services</h3>
    <ul>
      <li style="left:9px;top:57px">Data Recovery</li>
      <li style="left:9px;top:81px">Virus Removal</li>
      <li style="left:9px;top:106px">Recovery</li>
      <li style="left:9px;top:130px">System Installation</li>
    </ul>
  </div>
  <div class="service-col" style="left:359px">
    <h3>Nationwide IT<br>Services</h3>
    <ul>
      <li style="left:14px;top:57px">Recovery</li>
      <li style="left:14px;top:81px">System Installation</li>
      <li style="left:14px;top:106px">Data Recovery</li>
      <li style="left:14px;top:130px">Virus Removal</li>
    </ul>
  </div>
  <div class="service-col" style="left:524px">
    <h3>Computer Repair,<br>Installation</h3>
    <ul>
      <li style="left:16px;top:58px">System Installation</li>
      <li style="left:16px;top:82px">Data Recovery</li>
      <li style="left:16px;top:106px">Recovery</li>
      <li style="left:16px;top:131px">Viral Removal</li>
    </ul>
  </div>
  <a href="#" class="read-more" style="left:86px">Read More...</a>
  <a href="#" class="read-more" style="left:258px">Read More...</a>
  <a href="#" class="read-more" style="left:429px">Read More...</a>
  <a href="#" class="read-more" style="left:591px">Read More...</a>
</section>

<section class="info-box" style="left:93px">
  <h2>Welcome !</h2>
  <div class="info-body">
    <p class="info-intro">Lorem ipsum dolor sit amet, consectetur adipiscing elit.</p>
    <p class="info-text">Larkfield Circuitry is a local repair and service company for homes and small businesses. We fix slow, broken and infected computers, and we explain every step in plain words so you always know what was done, what it cost and how to keep your system healthy.</p>
    <p class="info-text">Bring your machine to our shop or book a visit at your home or office. We work with desktops, laptops and small networks, and we back up your data before any repair begins, so nothing you care about is ever put at risk during the work.</p>
    <a href="#" class="info-more">READ MORE....</a>
  </div>
</section>

<section class="info-box" style="left:324px">
  <h2>Services</h2>
  <div class="info-body">
    <p class="info-intro">Lorem ipsum dolor sit amet, consectetur adipiscing elit.</p>
    <ul class="info-list">
      <li>Data Recovery</li>
      <li>Virus Removal</li>
      <li>New System Installation</li>
      <li>Data Recovery</li>
      <li>Virus Removal</li>
      <li>New System Installation</li>
    </ul>
  </div>
</section>

<section class="info-box" style="left:554px">
  <h2>Support</h2>
  <div class="info-body">
    <p class="info-intro">Lorem ipsum dolor sit amet, consectetur adipiscing elit.</p>
    <p class="info-text">Need help right away? Our support team answers calls and emails every weekday and can often fix common problems remotely. For larger jobs we schedule an on-site visit that suits you and give a clear price before we start any work on your system.</p>
    <p class="info-text">Small businesses can sign up for regular check-ups that keep software updated, backups tested and networks secure. We keep notes on every machine we service, so each visit is faster and every future problem is easier to solve for you and your staff.</p>
    <a href="#" class="info-more">READ MORE....</a>
  </div>
</section>

<footer class="site-footer">
  <span class="copyright">Copyright Larkfield Circuitry , All Right Reserved</span>
  <nav class="footer-nav">
    <a href="#" style="left:385px">Home</a>
    <a href="#" style="left:438px">About</a>
    <a href="#" style="left:493px">Services</a>
    <a href="#" style="left:558px">Data Recovery</a>
    <a href="#" style="left:652px">Testimonials</a>
    <a href="#" style="left:738px">Contacts</a>
  </nav>
</footer>
<div class="footer-strip"></div>

</body>
</html>
```